Refresh web site from year 2003

Voltaro Works has a web site (https://vowrk-site.no/) from early 2000 that needs to be refreshed.

Attached are company logo, favicon files, a licensed image to be used, an animation that illustrate the use of one of the products.

Target Market(s)

Industrial customers

Industry/Entity Type

Electrical Switch Board Builders, Automation Industry

Coding

Coded - Design and coding required

Number of Pages Required

3 page

Requirements
Must have
• WordPress site. Use attached animation in the front page (source file is in Adobe Animation format, if adjustments are needed). Product page for two products, "KTR" and "QX-7 Ver B".
Nice to have
• The site should focus on promoting two products KTR and QX-7 Ver B.

```html
<!DOCTYPE html>
<html lang="en">
<head>
<meta charset="utf-8">
<title>Voltaro Works – Electronics Production Company</title>
<link href="https://fonts.googleapis.com/css2?family=Lato:wght@400;700;900&display=swap" rel="stylesheet">
<style>
:root{
  --navy:#0b3d6b;
  --blue:#0c4c86;
  --deep:#062447;
  --ink:#1a1a1a;
  --text:#333;
  --faint:#ececec;
  --white:#fff;
}
*{box-sizing:border-box;margin:0;padding:0}
html,body{width:1200px;height:4274px;overflow:hidden}
body{font-family:'Lato',sans-serif;color:var(--text);background:var(--white);position:relative}
.abs{position:absolute}
.center{text-align:center}
.btn-outline{position:absolute;border:2px solid var(--white);color:var(--white);font-weight:700;font-size:15px;display:flex;align-items:center;justify-content:center;letter-spacing:.3px}

/* header */
.site-header{position:absolute;left:0;top:0;width:1200px;height:66px;background:var(--white);z-index:3}
.brand{position:absolute;left:158px;top:18px;font-weight:900;font-size:22px;color:var(--navy)}
.nav a{position:absolute;top:24px;font-size:14px;font-weight:700;color:var(--ink);text-decoration:none}
.nav a.active{color:var(--blue)}
.call{position:absolute;left:777px;top:0;width:190px;height:56px;background:var(--navy);color:var(--white);font-size:14px;font-weight:700;display:flex;align-items:center;justify-content:center}
.flag{position:absolute;top:20px;width:26px;height:17px}

/* hero */
.hero-img{position:absolute;left:0;top:66px;width:1200px;height:573px;background:linear-gradient(120deg,#0e3f66 0%,#1d6f97 45%,#14557f 75%,#0c3c63 100%);clip-path:polygon(0 0,100% 0,100% 80.5%,50% 100%,0 80.5%)}
.hero-title{position:absolute;left:0;width:1200px;text-align:center;color:var(--white)}

/* products */
.ghost{position:absolute;font-weight:900;color:var(--faint);letter-spacing:2px}
.section-title{position:absolute;left:0;width:1200px;text-align:center;font-weight:900;color:var(--ink)}
.panel{position:absolute;top:772px;height:492px;width:442px}
.panel-left{left:158px;background:var(--navy);clip-path:polygon(0 0,100% 7.5%,100% 100%,0 100%)}
.panel-right{left:600px;background:var(--blue);clip-path:polygon(0 7.5%,100% 0,100% 100%,0 100%)}
.product-name{position:absolute;left:0;top:50px;width:100%;font-size:40px;color:var(--white);font-weight:400;text-align:center;line-height:50px}
.underline{position:absolute;left:197px;top:110px;width:48px;height:3px;background:var(--white)}
.product-photo{position:absolute;top:161px;width:122px;height:107px;background:var(--white);padding:8px}
.product-photo div{width:100%;height:100%;background:radial-gradient(circle at 45% 45%,#e9e3e3 0%,#b9a7a4 45%,#ffffff 75%)}
.features{position:absolute;top:158px;list-style:none;color:var(--white);font-size:16px}
.features li{position:relative;padding-left:22px;margin-bottom:16px;line-height:22px}
.features li::before{content:"";position:absolute;left:0;top:7px;width:7px;height:7px;border:1.5px solid var(--white);border-radius:50%}

/* welcome */
.welcome h2{position:absolute;left:158px;font-size:44px;font-weight:700;line-height:52px}
.welcome p{position:absolute;left:158px;top:1484px;width:455px;font-size:14.5px;line-height:24px;color:var(--ink)}
.read-more{position:absolute;left:158px;top:1681px;width:164px;height:48px;border:2px solid var(--blue);color:var(--blue);font-weight:700;font-size:15px;display:flex;align-items:center;justify-content:center}
.factory-photo{position:absolute;left:681px;top:1329px;width:360px;height:360px;border-radius:50%;background:linear-gradient(135deg,#cfd6da 0%,#8f9ea6 40%,#e6e9ea 70%,#aab4ba 100%);border:6px solid var(--white);box-shadow:0 0 12px rgba(0,0,0,.15)}
.badge{position:absolute;left:682px;top:1581px;width:140px;height:140px;border-radius:50%;background:var(--blue)}

/* services */
.services{position:absolute;left:0;top:1792px;width:1200px;height:498px;background:linear-gradient(160deg,#ffffff 0%,#f0f0f0 40%,#e6e6e6 70%,#f7f7f7 100%)}
.service{position:absolute;top:126px;width:210px}
.service .icon{width:66px;height:66px;border-radius:8px;background:linear-gradient(135deg,#f2b233,#3a6ea5)}
.service h3{margin-top:30px;font-size:22px;font-weight:700;color:var(--ink);letter-spacing:.5px;line-height:30px}
.service p{margin-top:20px;font-size:14px;line-height:22px;color:var(--ink)}

/* review */
.vertical-ghost{position:absolute;transform:rotate(-90deg);transform-origin:left top;font-weight:900;color:var(--faint);font-size:92px;letter-spacing:2px;white-space:nowrap}
.avatar{position:absolute;left:532px;top:2440px;width:136px;height:136px;border-radius:50%;border:3px solid var(--blue);padding:6px;background:var(--white)}
.avatar div{width:100%;height:100%;border-radius:50%;background:linear-gradient(180deg,#e8e8e8,#bdbdbd)}
.quote-mark{position:absolute;font-size:72px;font-weight:900;color:var(--blue);line-height:1}
.quote{position:absolute;left:315px;top:2595px;width:590px;text-align:center;font-size:14.5px;line-height:24px;color:var(--ink)}
.dot{position:absolute;left:1025px;width:16px;height:16px;border-radius:50%;border:1.5px solid var(--blue)}
.dot.on{background:var(--blue)}

/* newsletter */
.newsletter{position:absolute;left:0;top:2817px;width:1200px;height:369px;background:linear-gradient(130deg,#0a3f74 0%,#1560a4 35%,#0c4a88 60%,#06366a 100%)}
.mail-input{position:absolute;left:339px;top:153px;width:522px;height:65px;background:var(--white);display:flex;align-items:center;justify-content:center;font-size:17px;color:var(--ink)}

/* contact */
.map{position:absolute;left:252px;top:3252px;width:614px;height:520px;background:linear-gradient(135deg,#cfcfcf 0%,#bdbdbd 50%,#d6d6d6 100%)}
.form-box{position:absolute;left:565px;top:3288px;width:477px;height:442px;background:var(--blue)}
.field{position:absolute;background:var(--white);font-size:14px;color:var(--ink);padding:18px 0 0 14px}

/* footer */
.site-footer{position:absolute;left:0;top:3832px;width:1200px;height:442px;background:var(--deep);color:var(--white)}
.site-footer h4{position:absolute;top:118px;font-size:16px;font-weight:700;letter-spacing:.3px}
.site-footer .item{position:absolute;font-size:13px;line-height:18px}
.social-dot{position:absolute;width:22px;height:22px;border-radius:50%;border:2px solid var(--white)}
.rule{position:absolute;top:357px;height:1px;background:#5d7691}
</style>
</head>
<body>

<header class="site-header">
  <div class="brand">Voltaro Works</div>
  <nav class="nav">
    <a class="active" style="left:485px" href="#">HOME</a>
    <a style="left:566px" href="#">PRODUCTS</a>
    <a style="left:680px" href="#">CONTACT</a>
  </nav>
  <div class="call">CALL US :900 11 222</div>
  <div class="flag" role="img" aria-label="Norwegian language flag" style="left:982px;background:#c8102e"></div>
  <div class="flag" role="img" aria-label="English language flag" style="left:1015px;background:#1f3a7a"></div>
</header>

<section class="hero">
  <div class="hero-img" role="img" aria-label="Blue-toned photo of electrical switchboard cabinets"></div>
  <div class="hero-title" style="top:212px;font-size:38px;font-weight:400">WE ARE</div>
  <div class="hero-title" style="top:266px;font-size:52px;font-weight:900;line-height:62px">ELECTRONICS PRODUCTION<br>COMPANY</div>
  <div class="btn-outline" style="left:505px;top:420px;width:190px;height:47px">VIEW THE PRODUCTS</div>
</section>

<section class="products">
  <div class="ghost" style="left:0;width:1200px;text-align:center;top:668px;font-size:94px">PRODUCTS</div>
  <h2 class="section-title" style="top:694px;font-size:40px">PRODUCTS</h2>

  <div class="panel panel-left">
    <div class="product-name">KTR</div>
    <div class="underline"></div>
    <div class="product-photo" style="left:36px" role="img" aria-label="KTR lamp product photo"><div></div></div>
    <ul class="features" style="left:192px">
      <li>Easy installation</li>
      <li>Good view</li>
      <li>At an angle</li>
      <li>Low cost</li>
      <li>Save space and installation<br>Combine two lamps in one.</li>
    </ul>
    <div class="btn-outline" style="left:194px;top:393px;width:189px;height:48px">VIEW THE PRODUCTS</div>
  </div>

  <div class="panel panel-right">
    <div class="product-name">QX-7 Ver B</div>
    <div class="underline"></div>
    <ul class="features" style="left:42px">
      <li>Easy installation</li>
      <li>Good view</li>
      <li>At an angle</li>
      <li>Low cost</li>
      <li>Long life</li>
    </ul>
    <div class="product-photo" style="left:286px" role="img" aria-label="QX-7 Ver B lamp product photo"><div></div></div>
    <div class="btn-outline" style="left:42px;top:393px;width:190px;height:48px">VIEW THE PRODUCTS</div>
  </div>
</section>

<section class="welcome">
  <div class="ghost" style="left:150px;top:1325px;font-size:92px">WELCOME</div>
  <h2 style="top:1358px;color:var(--ink)">WELCOME TO THE</h2>
  <h2 style="top:1412px;color:var(--blue)">VOLTARO WORKS</h2>
  <p>Voltaro Works is a production and development company for electronics with an emphasis on small series production. We are currently 2 employees with good and relevant access to extra expertise in the established network. The company was established in 1985 and has since 2001 taken over production equipment and production basis from another company in the same industry.</p>
  <div class="read-more">READ MORE</div>
  <div class="factory-photo" role="img" aria-label="Photo of switchboard panels with indicator lamps"></div>
  <div class="badge"></div>
</section>

<section class="services">
  <div class="service" style="left:158px">
    <div class="icon" role="img" aria-label="Calculator icon"></div>
    <h3>Pressure<br>Calculator</h3>
    <p>Conversion table for the 9 most common pressure units.</p>
  </div>
  <div class="service" style="left:384px">
    <div class="icon" role="img" aria-label="Factory icon"></div>
    <h3>Production</h3>
    <p>Small series production of electronics units in the number of 10 to 200 units.</p>
  </div>
  <div class="service" style="left:606px">
    <div class="icon" role="img" aria-label="Development gears icon"></div>
    <h3>Development</h3>
    <p>Development of a product idea for a finished product in collaboration with a customer.</p>
  </div>
  <div class="service" style="left:830px">
    <div class="icon" role="img" aria-label="Design idea icon"></div>
    <h3>Design</h3>
    <p>Designing of electronics and printed circuit boards for pre-assembled and tested unit.</p>
  </div>
</section>

<section class="review">
  <div class="vertical-ghost" style="left:146px;top:2735px">REVIEW</div>
  <h2 class="section-title" style="top:2364px;font-size:40px;font-weight:700">CLIENT REVIEW</h2>
  <div class="avatar" role="img" aria-label="Client portrait"><div></div></div>
  <div class="quote-mark" style="left:276px;top:2580px">“</div>
  <p class="quote">Lorem Ipsum is simply dummy text of the printing and typesetting industry. Lorem Ipsum has been the industry's standard dummy text ever since the 1500s, when an unknown printer took a galley of type and scrambled it to make .</p>
  <div class="quote-mark" style="left:858px;top:2652px">”</div>
  <div class="abs center" style="left:0;width:1200px;top:2695px;font-size:22px;font-weight:700;color:var(--blue)">- ERIK MOEN</div>
  <div class="abs center" style="left:0;width:1200px;top:2726px;font-size:18px;color:var(--ink)">Businessman</div>
  <div class="dot on" style="top:2514px"></div>
  <div class="dot" style="top:2547px"></div>
  <div class="dot" style="top:2580px"></div>
</section>

<section class="newsletter" aria-label="Newsletter">
  <h2 class="section-title" style="top:85px;font-size:40px;font-weight:700;color:var(--white)">SIGN UP NEWSLETTER</h2>
  <div class="mail-input">Enter Your Mail ID</div>
  <div class="btn-outline" style="left:518px;top:234px;width:164px;height:47px">SUBSCRIBE NOW</div>
</section>

<section class="contact">
  <div class="vertical-ghost" style="left:146px;top:3745px">CONTACT</div>
  <div class="map" role="img" aria-label="Grey road map of the company location"></div>
  <div class="form-box">
    <h2 class="abs center" style="left:0;width:477px;top:28px;font-size:42px;font-weight:700;color:var(--white)">GET IN TOUCH</h2>
    <div class="field" style="left:42px;top:88px;width:193px;height:52px">Name :</div>
    <div class="field" style="left:243px;top:88px;width:192px;height:52px">Email :</div>
    <div class="field" style="left:42px;top:151px;width:393px;height:52px">Phone :</div>
    <div class="field" style="left:42px;top:214px;width:393px;height:146px">Message</div>
    <div class="btn-outline" style="left:144px;top:370px;width:190px;height:47px">SUBMIT NOW</div>
  </div>
</section>

<footer class="site-footer">
  <div class="abs" style="left:160px;top:100px;font-size:26px;font-weight:900">Voltaro Works</div>
  <p class="item" style="left:161px;top:178px;width:285px;line-height:21px">All the Lorem Ipsum generators on the Internet tend to repeat predefined chunks as necessary, making this the first true generator on the Internet.</p>

  <h4 style="left:515px">QUICK LINK</h4>
  <div class="item" style="left:515px;top:177px">»&nbsp;&nbsp;&nbsp;&nbsp;Home</div>
  <div class="item" style="left:515px;top:213px">»&nbsp;&nbsp;&nbsp;&nbsp;Products</div>
  <div class="item" style="left:515px;top:249px">»&nbsp;&nbsp;&nbsp;&nbsp;Contact</div>

  <h4 style="left:685px">CONTACT US</h4>
  <svg class="abs" style="left:684px;top:180px" width="12" height="16" viewBox="0 0 12 16"><path d="M6 0a6 6 0 0 0-6 6c0 4.5 6 10 6 10s6-5.5 6-10a6 6 0 0 0-6-6zm0 8.5A2.5 2.5 0 1 1 6 3.5a2.5 2.5 0 0 1 0 5z" fill="#fff"/></svg>
  <div class="item" style="left:716px;top:176px">Brekkeveien 40<br>4010 Holmvik Norway</div>
  <svg class="abs" style="left:684px;top:232px" width="13" height="13" viewBox="0 0 24 24"><path d="M6.6 10.8a15 15 0 0 0 6.6 6.6l2.2-2.2a1 1 0 0 1 1-.25 11.4 11.4 0 0 0 3.6.57 1 1 0 0 1 1 1V20a1 1 0 0 1-1 1A17 17 0 0 1 3 4a1 1 0 0 1 1-1h3.5a1 1 0 0 1 1 1c0 1.25.2 2.45.57 3.6a1 1 0 0 1-.25 1z" fill="#fff"/></svg>
  <div class="item" style="left:716px;top:230px">900 11 222</div>
  <svg class="abs" style="left:685px;top:268px" width="12" height="9" viewBox="0 0 12 9"><rect x=".5" y=".5" width="11" height="8" fill="none" stroke="#fff"/><path d="M.5.5 6 5l5.5-4.5" fill="none" stroke="#fff"/></svg>
  <div class="item" style="left:716px;top:264px">post@vowrk-site.no</div>

  <h4 style="left:933px">FOLLOW US</h4>
  <div class="social-dot" style="left:935px;top:178px"></div><div class="item" style="left:977px;top:181px">Friendbook</div>
  <div class="social-dot" style="left:935px;top:212px"></div><div class="item" style="left:977px;top:215px">Chirper</div>
  <div class="social-dot" style="left:935px;top:246px"></div><div class="item" style="left:977px;top:249px">Snapgram</div>
  <div class="social-dot" style="left:935px;top:280px"></div><div class="item" style="left:977px;top:283px">Worklink</div>

  <div class="rule" style="left:158px;width:325px"></div>
  <div class="item center" style="left:483px;width:234px;top:348px">© 2022 <b>VW</b>&nbsp; All rights reserved.</div>
  <div class="rule" style="left:717px;width:323px"></div>
</footer>

</body>
</html>
```